Optometric Practice needs Initial Photoshop Mockup

We need a graphic design for the homepage of a website for an optometric practice that specializes in vision therapy.

Here's the link to the project folder on Stashvale. I've included photos, example sites, content and instructions.

https://www.stashvale.example/sh/kx7rm2wq8zn41d9/BBQ_LmTyRwoPvXe3NcDrKuWjz

Please feel free to submit any questions about the design. I'll be happy to help guide you in any areas you're uncertain of.

Okay - I've updated the project to payment confirmed. Let's see some designs :) Thanks, Reg

```html
<!DOCTYPE html>
<html lang="en">
<head>
<meta charset="utf-8">
<title>Clearpath Vision Centers</title>
<link href="https://fonts.googleapis.com/css2?family=Raleway:wght@400;500;700;800&family=Open+Sans:wght@400;600;700&display=swap" rel="stylesheet">
<style>
:root{
  --red:#8c0f10;
  --red-dark:#6e0a0b;
  --blue:#3c5882;
  --navy:#1f3b86;
  --page:#f1ece3;
  --ink:#444;
  --muted:#8a8a8a;
  --white:#fff;
}
*{margin:0;padding:0;box-sizing:border-box}
html,body{width:750px;height:1200px;overflow:hidden}
body{position:relative;background:var(--page);font-family:"Open Sans",sans-serif;color:var(--ink)}
.abs{position:absolute}
.top-rule{left:0;top:0;width:750px;height:3px;background:var(--red)}
.appt-btn{left:546px;top:0;width:135px;height:27px;background:var(--red);color:#fff;font:500 11px "Raleway",sans-serif;display:flex;align-items:center;justify-content:center;border-radius:0 0 3px 3px}
.brand{left:64px;top:30px;display:flex;align-items:center;gap:10px}
.brand-mark{width:34px;height:34px;border-radius:50%;background:var(--red)}
.brand-name{font:700 22px "Raleway",sans-serif;color:var(--red);line-height:1}
.call{left:535px;top:42px;width:146px;height:40px}
.call-icon{position:absolute;left:0;top:0}
.call-text{position:absolute;right:0;top:4px;text-align:right;font-family:"Raleway",sans-serif;color:var(--blue)}
.call-text .label{font-size:14px;line-height:18px}
.call-text .num{font-size:15px;font-weight:500;line-height:18px}
.nav{left:62px;top:108px;width:624px;height:31px;background:var(--red);border-radius:3px 3px 0 0;display:flex;align-items:center;justify-content:space-between;padding:0 10px 0 7px;overflow:hidden}
.nav a{font:500 8.4px "Raleway",sans-serif;color:#fff;text-decoration:none;padding:5px 0;white-space:nowrap}
.nav a.active{background:#f3efe8;color:var(--red);border-radius:2px;padding:5px 9px}
.sheet{left:62px;top:139px;width:624px;height:895px;background:var(--white);box-shadow:0 1px 2px rgba(0,0,0,.08)}
.hero{left:69px;top:158px;width:612px;height:228px;background:linear-gradient(90deg,#8d6a52 0%,#b59a7a 35%,#cdbba3 55%,#c45a5e 75%,#b9413f 100%)}
.hero-line{left:78px;font:400 18px "Raleway",sans-serif;color:var(--blue);background:rgba(255,255,255,.82);padding:0 4px;height:21px;line-height:21px}
.hero-line b{color:var(--red);font-weight:800}
.tile{position:absolute}
.panel-blue{background:var(--blue);color:#fff;padding:14px 14px}
.panel-blue h2{font:400 15px "Raleway",sans-serif;margin-bottom:10px}
.panel-blue p{font-size:8.4px;line-height:15px}
.card{position:absolute;background:#fff;padding:14px 13px;box-shadow:0 0 2px rgba(0,0,0,.08)}
.card h3{font:500 12px "Raleway",sans-serif;color:var(--navy);margin-bottom:8px}
.card p{font-size:8.4px;line-height:15px;color:var(--muted);margin-bottom:9px}
.card a{font-size:8.4px;color:var(--navy);text-decoration:none}
.pointer{position:absolute;width:0;height:0;border-left:6px solid transparent;border-right:6px solid transparent}
.pointer.up{border-bottom:7px solid #fff}
.pointer.down{border-top:7px solid #fff}
.patient{font-size:7.5px;font-weight:700;line-height:11px;margin-top:12px}
.patient span{font-weight:600}
.patient-photo{position:absolute;right:10px;top:124px;width:58px;height:58px;border-radius:50%;background:radial-gradient(circle,#e8c39c,#b98a5e)}
.story-link{position:absolute;left:16px;bottom:22px;font-size:8.4px;color:#fff;text-decoration:underline}
.welcome h2{font:400 15px "Raleway",sans-serif;color:#555;margin-bottom:14px}
.welcome p{font-size:8.4px;line-height:15px;color:#555}
.video{left:406px;top:850px;width:276px;height:160px;background:linear-gradient(135deg,#3b4a66,#6b5a7a 45%,#2f3a52)}
.video-bar{position:absolute;left:0;bottom:0;width:100%;height:22px;background:rgba(0,0,0,.55)}
.tab{left:216px;top:1030px;width:268px;height:4px;background:var(--red);border-radius:3px 3px 0 0}
.foot h4{font:700 11px "Open Sans",sans-serif;color:#555;margin-bottom:8px}
.contact-row{display:flex;font-size:7.5px;line-height:13px;color:#555}
.contact-row .k{width:35px}.contact-row .c{width:10px}
.divider{width:1px;background:#cfc6b8}
.socials{display:flex;gap:5px}
.socials span{width:21px;height:21px;border-radius:50%;background:#6b6b6b;display:flex;align-items:center;justify-content:center}
.newsletter{font-size:8.4px;color:#555;margin:12px 0 6px}
.subscribe{display:flex;align-items:center}
.subscribe .field{width:110px;height:22px;background:#fff;font-size:7.5px;color:#444;padding-left:7px;line-height:22px}
.subscribe .go{font-size:9px;color:#777;margin-left:5px}
.foot-brand{font:700 14px "Raleway",sans-serif;color:#666;white-space:nowrap}
.copyright{font-size:7.5px;color:#555}
</style>
</head>
<body>
<div class="abs top-rule"></div>
<div class="abs appt-btn">Request An Appointment</div>

<div class="abs brand"><span class="brand-mark"></span><span class="brand-name">Clearpath Vision Centers</span></div>

<div class="abs call">
  <svg class="call-icon" width="40" height="40" viewBox="0 0 40 40"><circle cx="20" cy="20" r="18.5" fill="none" stroke="#3c5882" stroke-width="2.5"/><path d="M14 11c2-1 3 0 4 3 1 2 0 3-1 4 1 2 3 4 5 5 1-1 2-2 4-1 3 1 4 2 3 4-1 3-4 3-7 1-4-2-7-5-9-9-1-3 0-6 1-7z" fill="#3c5882"/></svg>
  <div class="call-text"><div class="label">Call Us Now</div><div class="num">410-555-0148</div></div>
</div>

<nav class="abs nav">
  <a class="active">Home</a><a>Meet Us</a><a>New Patients</a><a>Vision &amp; Learning</a><a>Vision Therapy</a><a>Head Injuries</a><a>Binocular Vision Disorders</a><a>Professionals</a><a>Contact Us</a>
</nav>

<div class="abs sheet"></div>

<div class="abs hero" role="img" aria-label="Smiling young woman reading in front of library bookshelves"></div>
<div class="abs hero-line" style="top:232px">Improving <b>VISION</b>, Changing <b>LIVES</b></div>
<div class="abs hero-line" style="top:262px">Improve Your <b>VISION</b> at Any <b>AGE</b></div>

<div class="tile panel-blue" style="left:69px;top:386px;width:205px;height:218px">
  <h2>About Us</h2>
  <p>Lorem ipsum dolor sit amet, consectetuer adipiscing elit, sed diam nonummy nibh euismod tincidunt ut laoreet dolore magna aliquam erat volutpat. Ut wisi enim ad minim veniam, quis nostrud exerci tation ullamcorper suscipit lobortis nisl ut aliquip ex ea commodo consequat. Duis autem vel eum iriure dolor in hendrerit in vulputate velit esse molestie consequat, vel illum dolore eu feugiat nulla facilisis</p>
</div>
<div class="tile" style="left:69px;top:604px;width:205px;height:110px;background:linear-gradient(135deg,#e6e2da,#a59b92 60%,#6d6a70)" role="img" aria-label="Woman reading papers at a desk"></div>
<div class="card" style="left:78px;top:720px;width:190px;height:96px">
  <span class="pointer up" style="left:22px;top:-7px"></span>
  <h3>Learning Related Problems</h3>
  <p>Lorem ipsum dolor sit amet, consectetuer adipiscing elit, sed diam</p>
  <a>Read More...</a>
</div>

<div class="tile" style="left:274px;top:386px;width:203px;height:108px;background:linear-gradient(135deg,#cfcfd6,#8d8f9a 60%,#3a3a40)" role="img" aria-label="Girl looking into a vision testing instrument"></div>
<div class="card" style="left:281px;top:501px;width:190px;height:96px">
  <span class="pointer up" style="left:24px;top:-7px"></span>
  <h3>Vision Therapy</h3>
  <p>Lorem ipsum dolor sit amet, consectetuer adipiscing elit, sed diam</p>
  <a>Read More...</a>
</div>
<div class="card" style="left:281px;top:611px;width:190px;height:96px">
  <span class="pointer down" style="left:18px;bottom:-7px"></span>
  <h3>Sport Vision</h3>
  <p>Lorem ipsum dolor sit amet, consectetuer adipiscing elit, sed diam nonummy nibh</p>
  <a>Read More...</a>
</div>
<div class="tile" style="left:274px;top:714px;width:203px;height:108px;background:linear-gradient(180deg,#b43a3e 0%,#a8454a 35%,#5f8a4e 40%,#7a9a5a 80%,#b08a66 100%)" role="img" aria-label="Baseball batter on a field"></div>

<div class="card" style="left:484px;top:392px;width:190px;height:96px">
  <span class="pointer down" style="left:20px;bottom:-7px"></span>
  <h3>Eye Examinations</h3>
  <p>Lorem ipsum dolor sit amet, consectetuer adipiscing elit, sed diam nonummy nibh</p>
  <a>Read More...</a>
</div>
<div class="tile" style="left:477px;top:494px;width:204px;height:110px;background:linear-gradient(90deg,#c7c3bf,#8e8a86 50%,#ddd6cc)" role="img" aria-label="Optometrist examining a patient with a slit lamp"></div>
<div class="tile panel-blue" style="left:477px;top:604px;width:204px;height:218px;padding:14px 16px">
  <h2>Success Stories</h2>
  <p>Lorem ipsum dolor sit amet, consectetuer adipiscing elit, sed diam nonummy nibh euismod tincidunt ut laoreet dolore magna aliquam erat volutpat. Ut wisi enim ad minim veniam, quis nostrud exerci tation ullamcorper</p>
  <div class="patient">MARINA HOLT<br><span>Patient</span></div>
  <div class="patient-photo" role="img" aria-label="Patient portrait"></div>
  <a class="story-link">Success with Vision Therapy</a>
</div>

<div class="abs welcome" style="left:69px;top:846px;width:312px">
  <h2 style="margin-left:2px">Welcome To Clearpath Vision Centers</h2>
  <p>Lorem ipsum dolor sit amet, consectetuer adipiscing elit, sed diam non-ummy nibh euismod tincidunt ut laoreet dolore magna aliquam erat volutpat. Ut wisi enim ad minim veniam, quis nostrud exerci tation ullamcorper suscipit lobortis nisl ut aliquip ex ea commodo consequat.<br>Lorem ipsum dolor sit amet, consectetuer adipiscing elit, sed diam non-ummy nibh euismod tincidunt ut laoreet dolore magna aliquam erat volutpat. Ut wisi enim ad minim veniam, quis nostrud exerci tation ullamcorper suscipit lobortis nisl ut aliquip ex ea commodo consequat.</p>
</div>
<div class="abs video" role="img" aria-label="Video of two news presenters in a studio">
  <svg style="position:absolute;left:116px;top:62px" width="44" height="30" viewBox="0 0 44 30"><rect width="44" height="30" rx="3" fill="rgba(0,0,0,.55)"/><path d="M17 8l12 7-12 7z" fill="#fff"/></svg>
  <div class="video-bar">
    <svg style="position:absolute;left:8px;top:5px" width="12" height="12" viewBox="0 0 12 12"><path d="M2 1l9 5-9 5z" fill="#fff"/></svg>
    <div style="position:absolute;left:58px;top:9px;width:147px;height:5px;background:#ddd"><div style="width:42px;height:5px;background:#1d9ad6"></div></div>
    <span style="position:absolute;right:8px;top:5px;font:700 italic 9px 'Open Sans',sans-serif;color:#1d9ad6">HD</span>
  </div>
</div>
<div class="abs tab"></div>

<div class="abs foot" style="left:89px;top:1064px">
  <h4>CONTACT US</h4>
  <div class="contact-row"><span class="k">Phone</span><span class="c">:</span><span>410-555-0148</span></div>
  <div class="contact-row"><span class="k">Email</span><span class="c">:</span><span>hello@clearpathvision.example</span></div>
  <div class="contact-row"><span class="k">Address</span><span class="c">:</span><span>4410 Meadowbrook Pkwy,<br>Harbor Center, Ste. 7<br>Lakewood, MD, 21099</span></div>
</div>
<div class="abs divider" style="left:284px;top:1060px;height:124px"></div>
<div class="abs foot" style="left:310px;top:1064px">
  <h4>GET IN TOUCH</h4>
  <div class="socials"><span></span><span></span><span></span>
    <span><svg width="12" height="9" viewBox="0 0 12 9"><rect x=".5" y=".5" width="11" height="8" fill="none" stroke="#fff"/><path d="M.5 .5l5.5 4.5 5.5-4.5" fill="none" stroke="#fff"/></svg></span>
  </div>
  <div class="newsletter">Subscribe monthly Newsletter</div>
  <div class="subscribe"><span class="field">Enter your email address</span><span class="go">GO</span></div>
</div>
<div class="abs divider" style="left:472px;top:1060px;height:124px"></div>
<div class="abs" style="left:492px;top:1094px;width:180px;text-align:center">
  <div class="foot-brand">Clearpath Vision Centers</div>
</div>
<div class="abs copyright" style="left:510px;top:1140px">Copyright © 2014 . All rights Reserved</div>
</body>
</html>
```